Emergency Vehicle Installer and Security Firm Needs a Business Card

Our company "Corvalt" need a business card for our Emergency Vehicle Equipment Installation and Infrastructure Security Business. We are contract designers, manufacturers and installers for Emergency Vehicle Fleets. This includes installation of Emergency Lights, Sirens, Vehicle Graphics and Radio Communications. We also supply this products to an international market. We also do consultant, and installation of high level security access, alarm and surveillance equipment for medium to large size businesses.

The design should represent a level of trust in our professionalism and expertise. It should visually display our ongoing relationship with the emergency services, but not overtake our commitment to high level security options.

Target Market(s)

Emergency Services and Businesses requiring high level security

Industry/Entity Type

Business

Contact Information for Business Card

*note complete details will be given to the winning designer for revising. The name "Mark Pell will be used to fill in name".

Mark Pell
Managing Director
Corvalt NZ Limited
Phone: +64 027 604 91352
Email: mark.pell@corvalt-example.co.nz

Requirements
Must have
• Card must be in black. Using our logo on the top as supplied. Designers should try having the reverse side as a blurred image of police lights (red and blue) with our logo in greyscale in the centre (this is not particularly a requirement, but feel free to play around with this option).
Nice to have
• A card design that looks good when spot UV printed. A clean compact and graphic design. A grey scale feel on the front (excluding logo, but you can play around with that idea). Rounded smooth text.
Should not have
• Will update this section as designs come through - feel free to submit what you feel would look good.

```html
<!DOCTYPE html>
<html lang="en">
<head>
<meta charset="utf-8">
<title>Corvalt – Business Card</title>
<link href="https://fonts.googleapis.com/css2?family=Open+Sans:wght@400;600;700&display=swap" rel="stylesheet">
<style>
  :root {
    --page: #dfe3e8;
    --card: #141414;
    --card-edge: #0b0b0b;
    --red: #d3282c;
    --white: #f4f4f4;
    --grey: #b9bcc2;
    --rule: #3a3a3a;
    --logo-dim: #3b3b3d;
  }
  * { margin: 0; padding: 0; box-sizing: border-box; }
  html, body { width: 793px; height: 1200px; overflow: hidden; }
  body {
    background: var(--page);
    font-family: "Open Sans", Arial, sans-serif;
    position: relative;
  }
  .card {
    position: absolute;
    width: 543px;
    height: 308px;
    background: linear-gradient(135deg, #222 0%, var(--card) 45%, var(--card-edge) 100%);
    overflow: hidden;
  }
  .card--front { left: 128px; top: 147px; }
  .card--back  { left: 130px; top: 756px; width: 541px; }

  .graphic-area {
    position: absolute;
    top: 0;
    height: 100%;
    background: linear-gradient(160deg, #e9ecef 0%, #9aa3ad 45%, #2b2b2b 100%);
  }
  .card--front .graphic-area { right: 0; width: 262px; }
  .card--back .graphic-area { left: 0; width: 258px;
    background: linear-gradient(200deg, #e9ecef 0%, #9aa3ad 45%, #2b2b2b 100%); }

  .brand {
    position: absolute;
    font-weight: 700;
    letter-spacing: 1px;
    line-height: 1;
  }
  .card--front .brand { left: 25px; top: 42px; font-size: 37px; color: var(--white); }

  .person__name {
    position: absolute; left: 26px; top: 114px;
    font-size: 16px; font-weight: 700; color: var(--red); letter-spacing: .5px;
  }
  .person__title {
    position: absolute; left: 26px; top: 136px;
    font-size: 12.5px; color: var(--white);
  }
  .divider {
    position: absolute; left: 26px; top: 168px;
    width: 218px; height: 1px; background: var(--rule);
  }
  .contacts { position: absolute; left: 27px; top: 187px; list-style: none; }
  .contacts li {
    display: flex; align-items: center; gap: 8px;
    height: 17px; font-size: 12.5px; color: var(--grey);
  }
  .contacts svg { width: 11px; height: 11px; flex: none; }
  .company {
    position: absolute; left: 28px; top: 245px;
    font-size: 12px; font-weight: 600; color: var(--red);
  }
  .address {
    position: absolute; left: 28px; top: 262px;
    font-size: 12.5px; color: var(--grey);
  }

  .card--back .brand { left: 266px; top: 128px; font-size: 40px; color: var(--logo-dim); }
  .tagline {
    position: absolute; left: 268px; top: 174px;
    font-size: 8px; font-weight: 700; letter-spacing: 1.5px; color: var(--logo-dim);
  }
</style>
</head>
<body>

<section class="card card--front" aria-label="Card front">
  <div class="graphic-area" role="img" aria-label="Large brand symbol in spot-UV white and black"></div>
  <div class="brand">CORVALT</div>
  <div class="person__name">MARK PELL</div>
  <div class="person__title">Managing Director</div>
  <div class="divider"></div>
  <ul class="contacts">
    <li>
      <svg viewBox="0 0 12 12"><rect width="12" height="12" rx="2" fill="var(--red)"/><path d="M3.5 3h1.6l.6 1.6-.9.7a4 4 0 0 0 1.9 1.9l.7-.9 1.6.6V8.5A1 1 0 0 1 8 9.4 5.5 5.5 0 0 1 2.6 4 1 1 0 0 1 3.5 3z" fill="#141414"/></svg>
      <span>+64 027 604 91352</span>
    </li>
    <li>
      <svg viewBox="0 0 12 12"><rect width="12" height="12" rx="2" fill="var(--red)"/><rect x="2.5" y="3.5" width="7" height="5" fill="none" stroke="#141414" stroke-width="1"/><path d="M2.5 3.5 6 6.3 9.5 3.5" fill="none" stroke="#141414" stroke-width="1"/></svg>
      <span>mark.pell@corvalt-example.co.nz</span>
    </li>
    <li>
      <svg viewBox="0 0 12 12"><rect width="12" height="12" rx="2" fill="var(--red)"/><circle cx="6" cy="6" r="3.4" fill="none" stroke="#141414" stroke-width="1"/><path d="M2.6 6h6.8M6 2.6c-1.6 2-1.6 4.8 0 6.8M6 2.6c1.6 2 1.6 4.8 0 6.8" fill="none" stroke="#141414" stroke-width=".8"/></svg>
      <span>www.corvalt-example.co.nz</span>
    </li>
  </ul>
  <div class="company">Corvalt NZ Limited</div>
  <div class="address">1/20 Sample Street, Any Town, Any City</div>
</section>

<section class="card card--back" aria-label="Card back">
  <div class="graphic-area" role="img" aria-label="Large brand symbol in spot-UV white and black"></div>
  <div class="brand">CORVALT</div>
  <div class="tagline">SEEN AND SECURE</div>
</section>

</body>
</html>
```